International Business Development Firm, in need of Branded Stationery material

We just made our Logo and now we are looking for branded stationery for our company such as:

* A Letterhead with our company's name, address, and logo at the top in Word format for easy editing
* A more formal letter format with a light background design (watermark) featuring our logo, allowing us to write over it for various documents and presentations
* Business card + Envelopes are a plus but not a must
* PowerPoint for company and product introductions
* An Info sheet with Bullet Points

The design should be professional.
Please ensure the design is high quality and print ready.

Target Market(s)

Businesses and high net value individuels

Industry/Entity Type

International Business Development Firm

Colors

Designer to choose colors to be used in the design.

Requirements
Must have
• word docs so i can use the stationery templates afterwards

```html
<!DOCTYPE html>
<html lang="en">
<head>
<meta charset="utf-8">
<title>Violetta Partners – Stationery Card</title>
<link rel="stylesheet" href="https://fonts.googleapis.com/css2?family=Montserrat:wght@600&family=Open+Sans:wght@700&family=Source+Sans+3:wght@400&display=swap">
<style>
  :root {
    --paper: #ececee;
    --edge: #c9c9cc;
    --violet: #6b4a95;
    --violet-band: #7f5ca8;
    --band-text: #e8e8ea;
  }
  html, body {
    margin: 0;
    padding: 0;
    width: 1200px;
    height: 904px;
    overflow: hidden;
    background: var(--paper);
  }
  .card {
    position: relative;
    width: 1200px;
    height: 904px;
    box-sizing: border-box;
    border: 1px solid var(--edge);
    background: var(--paper);
  }
  .brand-lockup {
    position: absolute;
    top: 130px;
    left: 0;
    width: 1200px;
    display: flex;
    justify-content: center;
    align-items: center;
    gap: 28px;
  }
  .brand-mark {
    width: 70px;
    height: 70px;
    background: var(--violet);
  }
  .brand-name {
    font-family: "Montserrat", sans-serif;
    font-weight: 600;
    color: var(--violet);
    text-transform: uppercase;
    letter-spacing: 1px;
    white-space: nowrap;
  }
  .brand-name--primary { font-size: 66px; }
  .tagline-band {
    position: absolute;
    top: 410px;
    left: 0;
    width: 1200px;
    height: 80px;
    background: var(--violet-band);
    display: flex;
    align-items: center;
    justify-content: center;
  }
  .tagline {
    margin: 0;
    font-family: "Open Sans", sans-serif;
    font-weight: 700;
    font-size: 44px;
    color: var(--band-text);
    letter-spacing: 0.2px;
  }
  .brand-name--secondary {
    position: absolute;
    top: 530px;
    left: 0;
    width: 1200px;
    text-align: center;
    font-size: 52px;
  }
  .contact {
    position: absolute;
    left: 52px;
    top: 688px;
    margin: 0;
    font-family: "Source Sans 3", sans-serif;
    font-style: normal;
    font-size: 42px;
    line-height: 52px;
    color: var(--violet);
  }
  .contact span { display: block; white-space: nowrap; }
</style>
</head>
<body>
  <main class="card">
    <header class="brand-lockup">
      <div class="brand-mark" aria-hidden="true"></div>
      <div class="brand-name brand-name--primary">Violetta Partners</div>
    </header>

    <section class="tagline-band">
      <h1 class="tagline">International Business Development Firm</h1>
    </section>

    <div class="brand-name brand-name--secondary">Violetta Partners</div>

    <address class="contact">
      <span>Address: aaaaaaaa, bbbbbbbb, cccccccccccc-</span>
      <span>Phone: 0000000000, E mail: violettapartners.com,</span>
      <span>Web: www.violettapartners.com</span>
    </address>
  </main>
</body>
</html>
```